Church Website with Home Page and Member Sermon Library

I am in need of an updated design for our church website. This will include 4 pages (outlined below). We are a conservative, evangelical, Christian church. The site should be modern and clean, while still reflecting our conservative values. I already have a logo for our church, and I want the site to incorporate the logo, and match the logo/branding. Stock photos are allowed if needed, but I have uploaded some images of our church and would prefer those images to be used if possible. Any stock photos used should not include any people in the photos (scenery, nature, buildings, animals, etc. are fine).

The site will need 4 pages: Home, Support Us (Donate), Login, and Recording Library.

Page 1: Home
The home page should include the following sections:

- Navigation: Should include links to each section of the home page plus a "listen live" link which will take the user to a live-streaming site and a "support us" link which will take the user to a support/donate page.

- Announcements: Can be either a banner or some other design, but there needs to be some way for us to post announcements for visitors to see. I'm open for creative ideas in this section, but would like it not to take up a lot of room on the page.

- About Us: Should include address, service times (see attached document), and information about the church.

- Pastor Bio: A section that introduces our pastor and gives a short bio about our pastor. Would like this section to include a picture of our pastor. Somewhere in this section I would like to include this Bible reference: "And I will give you pastors according to mine heart, which shall feed you with knowledge and understanding. Jer 3:15 KJV"

- Articles of Faith (What We Believe): This should include several sub-sections each with a heading, body, and possibly 1 or more scripture references. I have attached a document to the brief that includes our articles of faith. Feel free to be creative with this section in how you lay these out and format them.

- Support Us: A small section that explains what kind of support someone can give and a link to a donation page. The link can say something like "Support Us" or "Donate Now".

- Contact form: A contact form that allows the visitor to send us a message. The contact form should ask for name, email, phone, and message.

- Footer: A footer that will be displayed on all pages of the site. This should include at a minimum a link to the home page (or a link to each individual section in the home page if you prefer), a link to "listen live", a link to "support us", a link to "contact us" (or you can put the contact form directly in the footer if you prefer), the address, and a "member login" link.

Page 2: Support Us
The donation page should include a form the visitor can fill out to make a donation. We will embed a third party form later. For this design, please just mock out the design with a basic form asking for name, phone, and email.

Page 3: Login
The recording library (detailed below) will require members to login with a shared numeric code before accessing the page. We need a design for a login screen. The screen should include navigation/footer just like all other pages, but the body of the login page will consist only of a form that asks the user to enter the access code and then a "login" button.

Page 4: Recording Library

The library page is a member-only page that will require a shared, numeric pass code to access. On this page, members will be able to access a filterable list of past sermons. The page by default should display most recent sermons, but should also include a search form that allows the member to filter the sermon list to find a particular sermon. The search form should allow the user to select a filter type (e.g. Speaker name, date, event, etc.) and type in a value to search. They should be able to add multiple filters and remove filters that have been added. Each sermon that is displayed in the result list should include basic information such as title, date, speaker, tags, etc. along with a download icon, and an embedded audio player where they can click a play button to stream it on-demand. Each sermon should also have clickable tags associated with it that can be used to find related sermons.
Updates

I have uploaded several images of our church. Feel free to incorporate these into your design if possible.

Target Market(s)

Church Members

Industry/Entity Type

Religion

Number of Pages Required

4 page

Font styles to use
Sans Serif

Colors

Designer to choose colors to be used in the design.

Requirements
Must have
• Must incorporate the logo (attached)
Nice to have
• Would like the design to incorporate pictures of our church (attached) instead of stock photos if possible.
Should not have
• Please avoid an overly cluttered design. Stock photos used should not include any people in the photos.

```html
<!DOCTYPE html>
<html lang="en">
<head>
<meta charset="utf-8">
<title>Cedar Grace Church</title>
<link rel="stylesheet" href="https://fonts.googleapis.com/css2?family=Cinzel:wght@400;500&family=Poppins:wght@300;400;500;600&display=swap">
<style>
:root{
  --cyan:#03b4d6;
  --cyan-dark:#0398b6;
  --green-light:#86b26a;
  --green-dark:#3c6a24;
  --text:#333;
  --muted:#6b6b6b;
  --white:#fff;
  --hero-a:#6b4a26;
  --hero-b:#a9773f;
  --footer:#1d1d1f;
  --line:#d8d8d8;
}
*{box-sizing:border-box;margin:0;padding:0}
html,body{width:1200px;height:3551px;overflow:hidden}
body{font-family:"Poppins",sans-serif;color:var(--text);background:var(--white);position:relative}
section,footer{position:absolute;left:0;width:1200px}
.abs{position:absolute}
.serif{font-family:"Cinzel",serif;font-weight:400}
.btn{position:absolute;display:flex;align-items:center;justify-content:center;background:var(--cyan);color:var(--white);font-size:13px;font-weight:500;border-radius:2px;text-transform:uppercase;letter-spacing:.3px}
.title-two .l{color:var(--green-light)}
.title-two .d{color:var(--green-dark)}
.eyebrow{font-size:13px;color:var(--green-light);text-transform:uppercase}

/* hero */
.hero{top:0;height:610px;background:linear-gradient(180deg,var(--hero-a) 0%,#8c6233 45%,#b27a3b 75%,#7a5028 100%);overflow:hidden}
.hero-slant{left:560px;top:0;width:700px;height:610px;background:rgba(255,235,200,.14);clip-path:polygon(0 0,100% 0,100% 100%,157px 100%,157px 40%)}
.hero-arch{left:717px;top:124px;width:327px;height:486px;border-radius:163px 163px 0 0;background:radial-gradient(circle at 25% 22%,#fff7d6 0%,#ffcd5a 12%,#e58a23 35%,#a35618 70%,#3c2412 100%)}
.logo{left:161px;top:88px;width:150px;text-align:center;color:var(--white);font-size:15px;letter-spacing:3px;font-weight:400;line-height:1.4}
.nav{left:459px;top:50px;display:flex;gap:40px;font-size:13px;color:var(--white)}
.hero h1{left:163px;top:238px;font-size:52px;color:var(--white);letter-spacing:2px}
.hero p{left:163px;top:304px;width:510px;font-size:14.5px;line-height:25px;color:var(--white)}

/* about */
.about{top:610px;height:620px;background:linear-gradient(180deg,#fff 0%,#fff 40%,#efedea 70%,#f4f3f1 100%)}
.about-photo{left:0;top:260px;width:1200px;height:360px;background:linear-gradient(180deg,rgba(255,255,255,0) 0%,rgba(222,216,208,.55) 50%,rgba(238,236,232,.6) 100%)}
.center{left:0;width:1200px;text-align:center}
.about .eyebrow{top:84px}
.about h2{top:104px;font-size:36px}
.about .copy{left:210px;width:780px;top:170px;font-size:14px;line-height:24.5px;color:#333;text-align:center}
.about .copy p+p{margin-top:6px}
.address{top:310px;display:flex;justify-content:center;align-items:center;gap:10px;font-size:14px}
.pin{width:36px;height:36px;border:1.5px solid var(--green-dark);border-radius:50%;display:flex;align-items:center;justify-content:center}
.services{left:274px;top:440px;width:642px;height:97px;background:var(--cyan);border-radius:8px;overflow:hidden;color:var(--white);font-size:14px;font-weight:500}
.services .clock{position:absolute;left:0;top:0;width:110px;height:97px;background:var(--cyan-dark);border-radius:0 50px 50px 0;display:flex;align-items:center;justify-content:center}
.services .s{position:absolute;white-space:nowrap}

/* pastor */
.pastor{top:1230px;height:600px;background:#f6f6f6;border-bottom:1px solid #e6e6e6}
.pastor-photo{left:128px;top:67px;width:378px;height:533px;border-radius:150px 150px 0 0;background:linear-gradient(180deg,#bfe9f2 0%,#e9e9e6 35%,#f2f2f0 100%)}
.pastor .eyebrow{left:614px;top:130px}
.pastor h2{left:614px;top:146px;font-size:34px;color:var(--green-dark)}
.pastor .quote{left:614px;top:198px;width:430px;font-size:15.5px;font-weight:600;line-height:23px;color:#333}
.pastor .bio{left:614px;top:268px;width:430px;font-size:14px;line-height:24.5px;color:var(--muted)}

/* articles */
.articles{top:1830px;height:524px;background:var(--white)}
.articles h2{top:80px;font-size:36px}
.faith-list{left:161px;top:159px;width:199px;list-style:none;font-size:14px;color:#555}
.faith-list li{height:39px;line-height:38px;padding-left:11px;border-top:1px solid #e6e6e6}
.faith-list li:last-child{border-bottom:1px solid #e6e6e6}
.faith-list li.active{background:var(--cyan);color:var(--white);border-radius:3px;border-top-color:var(--cyan)}
.articles h3{left:429px;top:175px;font-size:32px;color:var(--green-dark)}
.articles .body{left:429px;top:225px;width:607px;font-size:14px;line-height:23px;color:var(--muted);text-align:justify}
.refs{position:absolute;font-size:14px;color:var(--muted);display:flex;align-items:center;gap:6px;white-space:nowrap}

/* support */
.support{top:2354px;height:342px;background:linear-gradient(180deg,#e4e4e4,#efefef 50%,#e8e8e8);border-top:1px solid #ddd}
.support .eyebrow{top:90px}
.support h2{top:108px;font-size:46px;color:var(--green-dark);font-weight:500}
.support p{left:240px;width:720px;top:172px;font-size:17px;line-height:30px;color:#555;text-align:center}

/* contact */
.contact{top:2696px;height:512px;background:var(--white)}
.contact h2{top:80px;font-size:36px}
.field{position:absolute;border:1.5px solid #d6d6d6;border-radius:3px;font-size:13px;color:#444;display:flex}
.field .ico{width:38px;border-right:1px solid #d6d6d6;display:flex;justify-content:center;padding-top:14px}
.field span{padding:13px 0 0 18px}

/* footer */
.footer{top:3208px;height:343px;background:radial-gradient(ellipse at 50% 30%,#2c2c2e 0%,var(--footer) 70%);color:#ddd}
.footer h4{position:absolute;font-size:18px;letter-spacing:2px;color:#eee;font-weight:400}
.footer .links a,.footer .info{position:absolute;font-size:13px;color:#ddd;text-decoration:none;white-space:nowrap}
.footer .flogo{left:809px;top:3310px;width:116px;text-align:center;font-size:14px;letter-spacing:2px;line-height:1.4;color:#eee}
.footer .stream{left:965px;top:146px;display:flex;align-items:center;gap:7px;font-size:17px;font-weight:600;color:#fff}
.footer .rule{left:163px;top:295px;width:874px;height:1px;background:#3a3a3a}
.footer .copy{left:0;width:1200px;top:310px;text-align:center;font-size:12px;color:#ccc}
</style>
</head>
<body>

<section class="hero">
  <div class="abs hero-slant"></div>
  <div class="abs hero-arch" role="img" aria-label="Sunset photograph of a cross on a rocky hill inside an arched frame"></div>
  <div class="abs logo">CEDAR GRACE<br>CHURCH</div>
  <nav class="abs nav"><span>Home</span><span>Donate</span><span>Login</span><span>Recording Library</span><span>Listen Live</span><span>Support Us</span></nav>
  <h1 class="abs serif">ANNOUNCEMENTS</h1>
  <p class="abs">Lorem ipsum dolor sit amet, consectetuer adipiscing elit sed diam nonummy nibh euismod tincidunt ut laoreet dolore magna aliquam erat volutpat. Ut wisi enim ad minim veniam.</p>
  <a class="btn" style="left:163px;top:404px;width:121px;height:36px">Know More</a>
</section>

<section class="about">
  <div class="abs about-photo" role="img" aria-label="Faded photograph of the church building"></div>
  <div class="abs center eyebrow">About Cedar</div>
  <h2 class="abs center serif title-two"><span class="l">GRACE</span> <span class="d">CHURCH</span></h2>
  <div class="abs copy">
    <p>Lorem ipsum dolor sit amet, consectetuer adipiscing elit, sed diam nonummy nibh euismod tincidunt ut laoreet dolore magna aliquam erat volutpat. Ut wisi enim ad minim veniam, quis nostrud exerci tation ullamcorper suscipit lobortis nisl ut aliquip ex ea commodo consequat.</p>
    <p>Duis autem vel eum iriure dolor in hendrerit in vulputate velit esse molestie consequat, vel illum dolore eu feugiat nulla facilisis at vero eros et accumsan et iusto odio dignissim qui blandit praesent.</p>
  </div>
  <div class="abs center address">
    <span class="pin"><svg width="14" height="18" viewBox="0 0 14 18"><path d="M7 0C3 0 0 3 0 7c0 5 7 11 7 11s7-6 7-11c0-4-3-7-7-7z" fill="#3c6a24"/><circle cx="7" cy="7" r="2.5" fill="#fff"/></svg></span>
    <span>42 Meadow Lane, Fairview, WY 82000 &nbsp;United States</span>
  </div>
  <a class="btn" style="left:528px;top:357px;width:144px;height:44px;font-size:15px;text-transform:none;border-radius:3px">Donate Now</a>
  <div class="abs services">
    <div class="clock"><svg width="42" height="42" viewBox="0 0 42 42"><circle cx="21" cy="21" r="18" fill="none" stroke="#fff" stroke-width="3.5"/><path d="M21 11v11h8" fill="none" stroke="#fff" stroke-width="3.5" stroke-linecap="round"/></svg></div>
    <div class="s" style="left:127px;top:14px">Service Times :</div>
    <div class="s" style="left:127px;top:39px">Wednesday Evening Service: 7:30 PM</div>
    <div class="s" style="left:127px;top:63px">Sunday School : 10:00 AM</div>
    <div class="s" style="left:412px;top:39px">Sunday Morning Service: 11:00</div>
    <div class="s" style="left:412px;top:63px">Sunday Evening Service: 5:30</div>
  </div>
</section>

<section class="pastor">
  <div class="abs pastor-photo" role="img" aria-label="Portrait photograph of the pastor"></div>
  <div class="abs eyebrow">Biography</div>
  <h2 class="abs serif">PASTOR BIO</h2>
  <p class="abs quote">"I will give you pastors according to mine heart, which shall feed you with knowledge and understanding. Jer 3:15 KJV"</p>
  <p class="abs bio">Lorem ipsum dolor sit amet, consectetuer adipiscing elit, sed diam nonummy nibh euismod tincidunt ut laoreet ore magna aliquam erat volutpat. Ut wisi enim ad minim ven quis nostrud exerci tation ullamcorper suscipit lobortis nisl ut aliquip ex ea commodo consequat. Duis autem vel eum iriuror in hendrerit in vulputate velit esse molestie consequat, vel illum dolore eu feugiat nulla facilisis at vero eros et accumsan.</p>
  <a class="btn" style="left:614px;top:463px;width:124px;height:36px">Contact Me</a>
</section>

<section class="articles">
  <h2 class="abs center serif title-two"><span class="l">ARTICLES</span> <span class="d">OF FAITH</span></h2>
  <ul class="abs faith-list">
    <li>The God Head.</li>
    <li class="active">Full Salvation.</li>
    <li>Sanctification.</li>
    <li>Baptism of the Holy Ghost.</li>
    <li>Divine Healing.</li>
    <li>Second coming of Christ.</li>
    <li>Eternity</li>
  </ul>
  <h3 class="abs serif">FULL SALVATION</h3>
  <p class="abs body">We believe that Salvation is received only when a person comes to the realization that he or she is lost and separated from God and becomes full of godly sorrow, confessing their sins and true repentance, believing in the shed blood of the Lord Jesus Christ as the only sacrifice for sins.Through the blood of Christ we have:</p>
  <div class="refs" style="left:429px;top:331px"><svg width="13" height="13" viewBox="0 0 13 13"><circle cx="6.5" cy="6.5" r="5.6" fill="none" stroke="#03b4d6" stroke-width="1.3"/><path d="M4 6.7l1.8 1.8L9.2 5" fill="none" stroke="#03b4d6" stroke-width="1.3"/></svg>Remission of Sins, Matthew 26:28 Heb 9:22</div>
  <div class="refs" style="left:429px;top:361px"><svg width="13" height="13" viewBox="0 0 13 13"><circle cx="6.5" cy="6.5" r="5.6" fill="none" stroke="#03b4d6" stroke-width="1.3"/><path d="M4 6.7l1.8 1.8L9.2 5" fill="none" stroke="#03b4d6" stroke-width="1.3"/></svg>Sanctification. Hebrews 13:12</div>
  <div class="refs" style="left:429px;top:391px"><svg width="13" height="13" viewBox="0 0 13 13"><circle cx="6.5" cy="6.5" r="5.6" fill="none" stroke="#03b4d6" stroke-width="1.3"/><path d="M4 6.7l1.8 1.8L9.2 5" fill="none" stroke="#03b4d6" stroke-width="1.3"/></svg>Redemption. Revelations 5:9</div>
  <div class="refs" style="left:789px;top:331px"><svg width="13" height="13" viewBox="0 0 13 13"><circle cx="6.5" cy="6.5" r="5.6" fill="none" stroke="#03b4d6" stroke-width="1.3"/><path d="M4 6.7l1.8 1.8L9.2 5" fill="none" stroke="#03b4d6" stroke-width="1.3"/></svg>Cleansing. 1 John 1:7 Rev. 1:5</div>
  <div class="refs" style="left:789px;top:361px"><svg width="13" height="13" viewBox="0 0 13 13"><circle cx="6.5" cy="6.5" r="5.6" fill="none" stroke="#03b4d6" stroke-width="1.3"/><path d="M4 6.7l1.8 1.8L9.2 5" fill="none" stroke="#03b4d6" stroke-width="1.3"/></svg>Justification. Romans 5:9</div>
</section>

<section class="support" role="img" aria-label="Faded photograph of a library interior">
  <div class="abs center eyebrow">Remaining to helps</div>
  <h2 class="abs center serif">SUPPORT US</h2>
  <p class="abs">Lorem ipsum dolor sit amet, consectetuer adipiscing elit, sed diam nonummy nibh euismod tincidunt ut laoreet dolore magna aliquam erat volutpat.</p>
  <a class="btn" style="left:538px;top:248px;width:124px;height:35px">Donate Now</a>
</section>

<section class="contact">
  <h2 class="abs center serif title-two"><span class="l">CONTACT</span> <span class="d">US</span></h2>
  <div class="field" style="left:284px;top:149px;width:308px;height:44px"><div class="ico"><svg width="11" height="12" viewBox="0 0 11 12"><circle cx="5.5" cy="3" r="3" fill="#9dbb86"/><path d="M0 12c0-4 2.5-5.5 5.5-5.5S11 8 11 12z" fill="#9dbb86"/></svg></div><span>First Name*</span></div>
  <div class="field" style="left:608px;top:149px;width:308px;height:44px"><div class="ico"><svg width="11" height="12" viewBox="0 0 11 12"><circle cx="5.5" cy="3" r="3" fill="#9dbb86"/><path d="M0 12c0-4 2.5-5.5 5.5-5.5S11 8 11 12z" fill="#9dbb86"/></svg></div><span>Last Name*</span></div>
  <div class="field" style="left:284px;top:207px;width:308px;height:44px"><div class="ico"><svg width="12" height="12" viewBox="0 0 12 12"><path d="M2 0l2.5 2.5-1.3 1.8c.8 1.8 2.3 3.3 4.1 4.1l1.8-1.3L12 10l-1.8 2C5 12 0 7 0 1.8z" fill="#9dbb86"/></svg></div><span>Your Phone*</span></div>
  <div class="field" style="left:608px;top:207px;width:308px;height:44px"><div class="ico"><svg width="13" height="10" viewBox="0 0 13 10"><rect width="13" height="10" rx="1" fill="#9dbb86"/><path d="M0 1l6.5 4.5L13 1" fill="none" stroke="#fff" stroke-width="1.2"/></svg></div><span>Your Email*</span></div>
  <div class="field" style="left:284px;top:266px;width:632px;height:88px"><div class="ico"><svg width="14" height="11" viewBox="0 0 14 11"><ellipse cx="5.5" cy="4" rx="5.5" ry="4" fill="#9dbb86"/><ellipse cx="9.5" cy="7" rx="4.5" ry="3.5" fill="#9dbb86"/></svg></div><span>Your Message</span></div>
  <a class="btn" style="left:538px;top:385px;width:124px;height:36px">Submit Now</a>
</section>

<footer class="footer">
  <h4 class="serif" style="left:163px;top:76px">QUICK LINKS</h4>
  <div class="links">
    <a style="left:163px;top:112px;text-decoration:underline">Home</a>
    <a style="left:163px;top:139px">Donate</a>
    <a style="left:163px;top:166px">Login</a>
    <a style="left:247px;top:112px">Recording Library</a>
    <a style="left:247px;top:139px">Listen Live</a>
    <a style="left:247px;top:166px">Support Us</a>
  </div>
  <h4 class="serif" style="left:490px;top:76px;font-size:17px">CONTACT INFO</h4>
  <div class="info" style="left:490px;top:112px;line-height:21px">42 Meadow Lane, Fairview, WY<br>82000 &nbsp;United States</div>
  <div class="info" style="left:490px;top:167px">info@cedargracechurch.org</div>
  <div class="info" style="left:490px;top:199px;font-size:16px">(555) 010-2040</div>
  <div class="abs" style="left:809px;top:128px;width:116px;text-align:center;font-size:14px;letter-spacing:2px;line-height:1.4;color:#eee">CEDAR GRACE<br>CHURCH</div>
  <div class="abs stream"><span style="width:14px;height:14px;border-radius:50%;background:#fff;display:inline-block"></span>Streamly</div>
  <div class="abs rule"></div>
  <div class="abs copy">© 2023 Cedar Grace Church. All Rights Reserved.</div>
</footer>

</body>
</html>
```